Meadow Reset sale graphics for social media

You MUST read the Brief in the WORD document and follow the instructions there. I want to create 10 social media graphics (new Instagram size 4:5 (1080 x 1350 pixels) focusing on our Mother’s Day Meadow Reset Sale graphics, using any of the pics attached. Use the attached pics, NO RANDOM STOCK PHOTOGRAPHY. For the color scheme of the graphics, they should all be complementary to the product colors or feel like Spring time.

Target Market(s)

primarily women

Requirements
Must have
• the photos and text attached

```html
<!DOCTYPE html>
<html lang="en">
<head>
<meta charset="utf-8">
<title>Meadow Reset Sale – Social Graphics Set</title>
<link rel="stylesheet" href="https://fonts.googleapis.com/css2?family=Montserrat:wght@800;900&family=Oswald:wght@600;700&family=Kaushan+Script&display=swap">
<style>
:root{
  --pink:#e23a7e;
  --green:#6dad36;
  --purple:#6a3d9e;
  --teal:#1f8790;
  --white:#ffffff;
  --ink-soft:#7a5aa8;
  --badge:#e5487f;
}
*{box-sizing:border-box;margin:0;padding:0}
html,body{width:1200px;height:1200px;overflow:hidden;background:var(--white)}
.board{position:relative;width:1200px;height:1200px}
.tile{position:absolute;overflow:hidden;display:flex;flex-direction:column;align-items:center;text-align:center;line-height:.95}
.num{position:absolute;left:10px;top:10px;width:22px;height:22px;border-radius:50%;background:var(--badge);color:var(--white);font:800 13px/22px Montserrat,sans-serif;text-align:center}
.wide{font-family:Montserrat,sans-serif;font-weight:900;letter-spacing:-.5px}
.cond{font-family:Oswald,sans-serif;font-weight:700;letter-spacing:.2px}
.script{font-family:"Kaushan Script",cursive;font-weight:400}
.pink{color:var(--pink)}.green{color:var(--green)}.purple{color:var(--purple)}.teal{color:var(--teal)}.soft{color:var(--ink-soft)}
.products{position:absolute;left:4%;right:4%;bottom:10px;border-radius:6px;background:linear-gradient(90deg,#f7d3df 0 12%,#eef6f7 12% 28%,#e9f1ee 28% 44%,#fbe3e1 44% 60%,#e3ecf8 60% 76%,#efe6f6 76% 100%)}
.brush{display:inline-block;padding:4px 22px;transform:rotate(-3deg);color:var(--white)}
.brush.green-band{background:var(--green)}
.brush.pink-band{background:var(--pink)}
.divider{display:flex;align-items:center;gap:8px;margin-top:8px}
.divider span{display:block;width:48px;height:1.5px;background:var(--purple)}
.divider svg{width:12px;height:11px}
.bg-mint{background:linear-gradient(180deg,#f3f8ef,#e9f3e2 70%,#f6f9f3)}
.bg-wood{background:linear-gradient(180deg,#f7f7f5,#ecedeb)}
.bg-leaf{background:linear-gradient(180deg,#f5f9ee,#e3f0d2)}
.bg-blush{background:linear-gradient(180deg,#fbeef3,#f6e2ea)}
.bg-lilac{background:linear-gradient(120deg,#efe9f7,#e4dbf1)}
.bg-sky{background:linear-gradient(180deg,#d9ecfa,#eef6fc)}
.bg-petal{background:linear-gradient(180deg,#f8f3f5,#f2e7ec)}
.portrait{position:absolute;right:0;top:14px;width:150px;bottom:0;background:linear-gradient(180deg,#3b2a26 0 30%,#c99275 30% 48%,#f3f1f4 48%);border-radius:70px 0 0 0}
</style>
</head>
<body>
<main class="board">

  <!-- 1 -->
  <section class="tile bg-mint" style="left:145px;top:30px;width:291px;height:410px;padding-top:36px">
    <div class="num">1</div>
    <div class="wide pink" style="font-size:20px">MOTHER’S DAY</div>
    <div class="wide green" style="font-size:48px;margin-top:4px">MEADOW</div>
    <div class="wide pink" style="font-size:30px;margin-top:4px">RESET SALE</div>
    <div class="wide purple" style="font-size:76px;margin-top:4px;display:flex;align-items:flex-end">25<span style="font-size:28px;line-height:1.05;display:flex;flex-direction:column">%<span style="font-size:18px">OFF</span></span></div>
    <div class="brush green-band script" style="font-size:26px;margin-top:8px">Everything!</div>
    <div class="products" role="img" aria-label="Row of six supplement bottles and a pink cream tube" style="height:100px"></div>
  </section>

  <!-- 2 -->
  <section class="tile bg-wood" style="left:445px;top:30px;width:314px;height:410px;padding-top:50px">
    <div class="num">2</div>
    <div class="cond pink" style="font-size:64px">25% OFF</div>
    <div class="cond soft" style="font-size:32px;margin-top:6px">MOTHER’S DAY</div>
    <div class="wide green" style="font-size:46px;margin-top:6px">MEADOW</div>
    <div class="wide pink" style="font-size:32px;margin-top:4px">RESET SALE</div>
    <div class="divider"><span></span><svg viewBox="0 0 12 11"><path d="M6 11 0 4.5A3 3 0 0 1 6 1.5 3 3 0 0 1 12 4.5Z" fill="#6a3d9e"/></svg><span></span></div>
    <div class="products" role="img" aria-label="Row of six supplement bottles and a pink cream tube" style="height:112px"></div>
  </section>

  <!-- 3 -->
  <section class="tile bg-leaf" style="left:767px;top:30px;width:295px;height:410px;padding-top:44px">
    <div class="num">3</div>
    <div class="cond purple" style="font-size:96px">25%</div>
    <div class="cond purple" style="font-size:66px;margin-top:2px">OFF</div>
    <div class="brush green-band cond" style="font-size:22px;margin-top:10px">ALL SUPPLEMENTS</div>
    <div class="script purple" style="font-size:22px;margin-top:12px">Meadow Reset Sale! <span style="color:#f0c24a">✦</span></div>
    <div class="products" role="img" aria-label="Row of six supplement bottles and a pink cream tube" style="height:100px"></div>
  </section>

  <!-- 4 -->
  <section class="tile bg-leaf" style="left:145px;top:449px;width:289px;height:361px;padding-top:50px">
    <div class="num">4</div>
    <div class="cond teal" style="font-size:62px">25% OFF</div>
    <div class="cond pink" style="font-size:24px;margin-top:6px">MEADOW RESET SALE:</div>
    <div class="cond teal" style="font-size:36px;margin-top:14px">SPRING RESET.</div>
    <div class="cond purple" style="font-size:36px;margin-top:6px">SUMMER READY</div>
    <div class="products" role="img" aria-label="Row of six supplement bottles and a pink cream tube" style="height:104px"></div>
  </section>

  <!-- 5 -->
  <section class="tile bg-blush" style="left:442px;top:449px;width:274px;height:361px;padding-top:30px">
    <div class="num">5</div>
    <div class="wide pink" style="font-size:72px">25%</div>
    <div class="wide pink" style="font-size:72px">OFF</div>
    <div class="brush pink-band wide" style="font-size:19px;margin-top:4px">EVERYTHING:</div>
    <div class="wide purple" style="font-size:19px;margin-top:8px">MOTHER’S DAY</div>
    <div class="cond green" style="font-size:22px;margin-top:4px">MEADOW RESET SALE</div>
    <div class="products" role="img" aria-label="Row of six supplement bottles and a pink cream tube" style="height:86px"></div>
  </section>

  <!-- 6 -->
  <section class="tile bg-lilac" style="left:725px;top:449px;width:337px;height:361px;padding-top:46px;align-items:flex-start">
    <div class="num">6</div>
    <div class="portrait" role="img" aria-label="Smiling woman in a white sweater, hand at her chin"></div>
    <div style="width:170px;display:flex;flex-direction:column;align-items:center;margin-left:10px;position:relative">
      <div class="cond purple" style="font-size:40px">25% OFF</div>
      <div class="cond pink" style="font-size:17px;margin-top:4px">MOTHER’S DAY SALE:</div>
      <div class="script purple" style="font-size:30px;margin-top:14px">Feel Amazing</div>
      <div class="cond pink" style="font-size:36px;margin-top:6px">AGAIN!</div>
      <div class="divider"><span style="width:32px"></span><svg viewBox="0 0 12 11"><path d="M6 11 0 4.5A3 3 0 0 1 6 1.5 3 3 0 0 1 12 4.5Z" fill="#6a3d9e"/></svg><span style="width:32px"></span></div>
    </div>
    <div class="products" role="img" aria-label="Row of five supplement bottles and a pink cream tube" style="height:94px;right:30%"></div>
  </section>

  <!-- 7 -->
  <section class="tile bg-mint" style="left:145px;top:820px;width:212px;height:357px;padding-top:34px">
    <div class="num">7</div>
    <div class="cond pink" style="font-size:42px">25% OFF</div>
    <div class="cond teal" style="font-size:17px;margin-top:4px">MOTHER’S DAY SALE:</div>
    <div class="script pink" style="font-size:34px;margin-top:12px">Refresh</div>
    <div class="script purple" style="font-size:32px;margin-top:8px">Your Body</div>
    <div class="divider"><span style="width:42px"></span><svg viewBox="0 0 12 11"><path d="M6 11 0 4.5A3 3 0 0 1 6 1.5 3 3 0 0 1 12 4.5Z" fill="#6a3d9e"/></svg><span style="width:42px"></span></div>
    <div class="products" role="img" aria-label="Row of six supplement bottles and a pink cream tube" style="height:88px"></div>
  </section>

  <!-- 8 -->
  <section class="tile bg-sky" style="left:366px;top:820px;width:235px;height:357px;padding-top:30px">
    <div class="num">8</div>
    <div class="cond teal" style="font-size:42px">25% OFF</div>
    <div class="cond pink" style="font-size:17px;margin-top:2px">MEADOW RESET SALE:</div>
    <div class="wide green" style="font-size:30px;margin-top:12px">SPRING</div>
    <div class="wide green" style="font-size:30px">CLEANSE.</div>
    <div class="wide purple" style="font-size:30px">SUMMER</div>
    <div class="wide purple" style="font-size:30px">GLOW</div>
    <div class="divider"><span style="width:40px"></span><svg viewBox="0 0 12 11"><path d="M6 11 0 4.5A3 3 0 0 1 6 1.5 3 3 0 0 1 12 4.5Z" fill="#6a3d9e"/></svg><span style="width:40px"></span></div>
    <div class="products" role="img" aria-label="Row of six supplement bottles and a pink cream tube" style="height:86px"></div>
  </section>

  <!-- 9 -->
  <section class="tile bg-leaf" style="left:610px;top:820px;width:205px;height:357px;padding-top:30px">
    <div class="num">9</div>
    <div class="cond purple" style="font-size:38px">25% OFF</div>
    <div class="cond pink" style="font-size:15px;margin-top:4px">MOTHER’S DAY SALE:</div>
    <div class="cond teal" style="font-size:18px;margin-top:18px">DETOX THIS SPRING.</div>
    <div class="wide pink" style="font-size:27px;margin-top:8px">SHINE</div>
    <div class="wide pink" style="font-size:27px">THIS</div>
    <div class="wide pink" style="font-size:27px">SUMMER</div>
    <div class="products" role="img" aria-label="Row of six supplement bottles and a pink cream tube" style="height:86px"></div>
  </section>

  <!-- 10 -->
  <section class="tile bg-petal" style="left:824px;top:820px;width:238px;height:357px;padding-top:30px">
    <div class="num">10</div>
    <div class="cond pink" style="font-size:42px">25% OFF</div>
    <div class="cond purple" style="font-size:16px;margin-top:4px">MOTHER’S DAY SALE:</div>
    <div class="wide green" style="font-size:28px;margin-top:10px">MEADOW</div>
    <div class="wide green" style="font-size:30px">RESET</div>
    <div class="divider" style="margin-top:4px"><span style="width:22px;background:var(--green)"></span><span class="wide green" style="width:auto;height:auto;background:none;font-size:14px">FOR A</span><span style="width:22px;background:var(--green)"></span></div>
    <div class="wide purple" style="font-size:28px;margin-top:4px">SUMMER</div>
    <div class="wide purple" style="font-size:28px">BODY</div>
    <div class="divider"><span style="width:40px"></span><svg viewBox="0 0 12 11"><path d="M6 11 0 4.5A3 3 0 0 1 6 1.5 3 3 0 0 1 12 4.5Z" fill="#6a3d9e"/></svg><span style="width:40px"></span></div>
    <div class="products" role="img" aria-label="Row of six supplement bottles and a pink cream tube" style="height:80px"></div>
  </section>

</main>
</body>
</html>
```